Business card design for immigration consulting business

We need business card design for a company called T&R Migration Advisors Inc. This is a boutique immigration consulting and foreign recruitment agency owned and managed by two partners.
The business card will be used by partners \ owners of the business. The best way to describe the business would be committed to client, passionate about providing top-notch services, engaging, competent, professional

Target Market(s)

We work with individuals in and outside of Canada who need immigration advise as well as Canadian businesses looking to hire or sponsor foreign workers to Canada

Industry/Entity Type

Consulting

Contact Information for Business Card

The business card should have a standard size and horizontal lay-out

Font styles to use
Serif

Colors
f04a50
ec1f27
cbcbcb
dbdbdb

Requirements
Must have
• The business card mush have our logo, name of the company first and last name of the partner, position, phone, cell, fax, e-mail, skype, web-site
• Our first choice would a classic design with minimalist looks and elegant fonts and colors, but we are open minded to any creative ideas too
Nice to have
• On the other side it may have the description of the company: Immigration and Foreign Recruitment Services
• We're considering using stamping \ lettering on our business cards
• It would be nice if the business card would have white space, in case someone would like to make notes on it.
• One (back side) side of the business card can be all red with white logo
Should not have
• We do not want to have our pictures on the business card
• We do no want to have Canadian maple leaf on the business card as we already have one in our logo

```html
<!DOCTYPE html>
<html lang="en">
<head>
<meta charset="utf-8">
<title>T&amp;R Migration Advisors Inc. – Business Card</title>
<link rel="stylesheet" href="https://fonts.googleapis.com/css2?family=Tinos:wght@400&family=Open+Sans:wght@400;700&display=swap">
<style>
  :root {
    --red: #e1002f;
    --red-deep: #d10029;
    --paper: #f2f2f2;
    --paper-light: #fafafa;
    --ink: #4a4a4a;
    --logo-grey: #5e5e5e;
    --backdrop: #e6e6e6;
    --white: #ffffff;
  }
  * { box-sizing: border-box; margin: 0; padding: 0; }
  html, body {
    width: 1200px;
    height: 900px;
    overflow: hidden;
    background: var(--backdrop);
  }
  .canvas {
    position: relative;
    width: 1200px;
    height: 900px;
  }
  .card {
    position: absolute;
    left: 290px;
    width: 620px;
    height: 354px;
    overflow: hidden;
    box-shadow: 0 2px 6px rgba(0,0,0,0.12);
  }
  .card--front {
    top: 76px;
    background: linear-gradient(160deg, var(--red) 0%, var(--red-deep) 100%);
  }
  .card--back {
    top: 470px;
    background: linear-gradient(160deg, var(--paper-light) 0%, var(--paper) 100%);
  }
  .brand-name {
    position: absolute;
    left: 0;
    right: 0;
    text-align: center;
    font-family: "Tinos", "Times New Roman", serif;
    font-weight: 400;
    letter-spacing: 1px;
    white-space: nowrap;
  }
  .card--front .brand-name {
    top: 146px;
    font-size: 44px;
    color: var(--white);
  }
  .card--back .brand-name {
    top: 30px;
    font-size: 36px;
    color: var(--logo-grey);
  }
  .name-band {
    position: absolute;
    left: 0;
    right: 0;
    top: 100px;
    height: 84px;
    background: var(--red);
    display: flex;
    align-items: flex-end;
    justify-content: center;
    padding-bottom: 22px;
    font-family: "Open Sans", Arial, sans-serif;
    color: var(--white);
  }
  .person-name {
    font-weight: 700;
    font-size: 22px;
    line-height: 26px;
  }
  .person-role {
    font-size: 16px;
    margin-left: 10px;
    padding-left: 10px;
    border-left: 1px solid var(--white);
    line-height: 18px;
    margin-bottom: 2px;
  }
  .details {
    position: absolute;
    left: 0;
    right: 0;
    top: 204px;
    display: flex;
    justify-content: center;
    align-items: center;
    font-family: "Open Sans", Arial, sans-serif;
    color: var(--ink);
    font-size: 14px;
    line-height: 24px;
  }
  .address {
    font-style: normal;
    text-align: right;
    padding: 4px 20px 4px 0;
    border-right: 1px solid var(--ink);
  }
  .contact-list {
    list-style: none;
    padding-left: 20px;
  }
  .contact-item {
    display: flex;
    align-items: center;
    gap: 10px;
    white-space: nowrap;
  }
  .contact-label {
    color: var(--red);
    font-weight: 700;
    width: 14px;
  }
  .contact-icon {
    width: 14px;
    height: 14px;
    flex: none;
  }
</style>
</head>
<body>
<main class="canvas">
  <section class="card card--front" aria-label="Card front">
    <h1 class="brand-name">T&amp;R Migration Advisors Inc.</h1>
  </section>

  <section class="card card--back" aria-label="Card back">
    <h2 class="brand-name">T&amp;R Migration Advisors Inc.</h2>
    <div class="name-band">
      <span class="person-name">Daniel Hart</span>
      <span class="person-role">Manager</span>
    </div>
    <div class="details">
      <address class="address">
        214 Harbour Lane, Suite 8<br>
        Westbrook, ON L4K 2R7.
      </address>
      <ul class="contact-list">
        <li class="contact-item">
          <svg class="contact-icon" viewBox="0 0 24 24" aria-hidden="true"><path fill="#e1002f" d="M6.6 10.8a15.1 15.1 0 0 0 6.6 6.6l2.2-2.2c.3-.3.7-.4 1-.2 1.1.4 2.3.6 3.6.6.6 0 1 .4 1 1V20c0 .6-.4 1-1 1A17 17 0 0 1 3 4c0-.6.4-1 1-1h3.5c.6 0 1 .4 1 1 0 1.3.2 2.5.6 3.6.1.3 0 .7-.2 1z"/></svg>
          <span>T: +1 905 555 0148</span>
        </li>
        <li class="contact-item">
          <svg class="contact-icon" viewBox="0 0 24 24" aria-hidden="true"><rect x="6" y="1.5" width="12" height="21" rx="2.5" fill="#e1002f"/><rect x="8" y="4" width="8" height="13" fill="#fff"/><circle cx="12" cy="19.5" r="1.2" fill="#fff"/></svg>
          <span>C: +1 416 555 0192</span>
        </li>
        <li class="contact-item">
          <svg class="contact-icon" viewBox="0 0 24 24" aria-hidden="true"><rect x="6" y="2" width="12" height="6" fill="#e1002f"/><rect x="2" y="8" width="20" height="10" rx="2" fill="#e1002f"/><rect x="6" y="14" width="12" height="8" fill="#fff" stroke="#e1002f" stroke-width="2"/></svg>
          <span>F: +1 905 555 0177</span>
        </li>
        <li class="contact-item">
          <svg class="contact-icon" viewBox="0 0 24 24" aria-hidden="true"><rect x="2" y="5" width="20" height="14" rx="2" fill="#e1002f"/><path d="M3 6l9 7 9-7" fill="none" stroke="#fff" stroke-width="2"/></svg>
          <span>info@trmigration.com</span>
        </li>
        <li class="contact-item">
          <svg class="contact-icon" viewBox="0 0 24 24" aria-hidden="true"><path fill="#e1002f" d="M4 3h16a2 2 0 0 1 2 2v10a2 2 0 0 1-2 2H10l-5 4v-4H4a2 2 0 0 1-2-2V5a2 2 0 0 1 2-2z"/></svg>
          <span>Skype: trmigration.dhart</span>
        </li>
        <li class="contact-item">
          <svg class="contact-icon" viewBox="0 0 24 24" aria-hidden="true"><circle cx="12" cy="12" r="10" fill="#e1002f"/><path d="M2 12h20M12 2c3 3 3 17 0 20M12 2c-3 3-3 17 0 20" fill="none" stroke="#fff" stroke-width="1.5"/></svg>
          <span>www.trmigration.com</span>
        </li>
      </ul>
    </div>
  </section>
</main>
</body>
</html>
```